K & M Tire Shop business cards

need business card for tire/car care company based in tampa, florida. we sell used and new tires, also we service vehicles, tune ups, oil chasnge, brakes and A/c we offer free towing with major vehicle repair and tire purchase. we also offer free estimates on any engine or a/c repair. also we have the lowest price in the city on used and new tires.

Industry/Entity Type

Business

Contact Information for Business Card

4187 N Crestwell Ave,
Tampa, Fl 33829
Ph: 813-572-6148
KandMTireShop@examplemail.com

Font styles to use
Serif
Sans Serif
Decorative

Requirements
Must have
• my logo, what we do ( used and new tires , oil change, brakes, tune ups, free towing vehicl. Also business info.
Nice to have
• an image of a towing truck, highlighting that we offer free towing. something close to what i have in one of the attached image

```html
<!DOCTYPE html>
<html lang="en">
<head>
<meta charset="UTF-8">
<title>K & M Tire Shop – Business Cards</title>
<link href="https://fonts.googleapis.com/css2?family=Open+Sans:wght@400;700&display=swap" rel="stylesheet">
<style>
  :root {
    --bg: #d9d5d1;
    --yellow: #f4c81f;
    --black: #0d0d0d;
    --white: #ffffff;
    --ink: #2a2a2a;
    --photo-light: #e9ecef;
    --photo-mid: #8e98a6;
    --photo-blue: #3d5a99;
  }
  html, body {
    margin: 0;
    width: 1200px;
    height: 800px;
    overflow: hidden;
    background: var(--bg);
    font-family: "Open Sans", Arial, sans-serif;
  }
  .stage {
    position: relative;
    width: 1200px;
    height: 800px;
  }
  .card {
    position: absolute;
    top: 240px;
    width: 525px;
    height: 300px;
    overflow: hidden;
    box-shadow: 0 6px 18px rgba(0,0,0,0.18);
  }
  .card--front { left: 50px; background: var(--yellow); }
  .card--back  { left: 625px; background: var(--yellow); }
  .card__art {
    position: absolute;
    inset: 0;
  }
  .brand {
    position: absolute;
    display: flex;
    align-items: center;
    gap: 10px;
    font-family: "Open Sans", Arial, sans-serif;
    font-weight: 700;
    color: var(--black);
    white-space: nowrap;
  }
  .brand__dot {
    border-radius: 50%;
    background: var(--black);
    flex: none;
  }
  .card--front .brand {
    left: 300px;
    top: 42px;
    font-size: 21px;
  }
  .card--front .brand__dot { width: 20px; height: 20px; }
  .services {
    position: absolute;
    left: 300px;
    top: 100px;
    margin: 0;
    padding: 0;
    list-style: none;
    font-size: 15px;
    line-height: 1.3;
    color: var(--ink);
  }
  .services li::before { content: "- "; }
  .card--back .brand {
    left: 0;
    right: 0;
    top: 58px;
    justify-content: center;
    font-size: 34px;
  }
  .card--back .brand__dot { width: 30px; height: 30px; }
  .contact {
    position: absolute;
    left: 0;
    right: 0;
    top: 128px;
    margin: 0;
    text-align: center;
    font-style: normal;
    font-size: 15px;
    line-height: 1.45;
    color: var(--ink);
  }
  .back-band {
    position: absolute;
    left: 0;
    right: 0;
    bottom: 22px;
    height: 48px;
    background: var(--black);
  }
</style>
</head>
<body>
<main class="stage">

  <section class="card card--front" aria-label="Business card front">
    <svg class="card__art" viewBox="0 0 525 300" width="525" height="300">
      <defs>
        <linearGradient id="photoTone" x1="0" y1="0" x2="1" y2="1">
          <stop offset="0" stop-color="#e9ecef"/>
          <stop offset="0.55" stop-color="#8e98a6"/>
          <stop offset="1" stop-color="#3d5a99"/>
        </linearGradient>
      </defs>
      <path class="curve-band" d="M0 0 H305 C255 120 190 220 0 255 Z" fill="var(--black)"/>
      <path class="curve-white" d="M0 0 H280 C235 110 170 200 0 232 Z" fill="var(--white)"/>
      <path class="photo" role="img" aria-label="Photo of a mechanic's hand holding a wrench beside stacked tires and a blue tow truck"
            d="M20 20 H250 C215 105 160 175 20 200 Z" fill="url(#photoTone)"/>
    </svg>
    <div class="brand"><span class="brand__dot"></span>K &amp; M Tire Shop</div>
    <ul class="services">
      <li>Used and new tires</li>
      <li>Oil change,</li>
      <li>Brakes,</li>
      <li>Tune Ups,</li>
      <li>Free Towing with<br>&nbsp;&nbsp;major vehicle Repair</li>
      <li>Tire Purchase</li>
    </ul>
  </section>

  <section class="card card--back" aria-label="Business card back">
    <div class="brand"><span class="brand__dot"></span>K &amp; M Tire Shop</div>
    <address class="contact">
      4187 N Crestwell Ave, Tampa, Fl 33829<br>
      Ph: 813-572-6148<br>
      KandMTireShop@examplemail.com
    </address>
    <div class="back-band"></div>
  </section>

</main>
</body>
</html>
```